依頼詳細
ダイナミックなチラシとポスターをお願いします。
見ただけで「すごい!講演に行ってみたい!!」と思えるような。
記載項目
添付資料のとおり
サイズ
A2ポスターとA4チラシ
ページ数
片面
希望イメージ
シンプル 複雑
単色 カラフル
暗い 明るい
日常 高級
遊び心 厳粛
未来的 伝統的
女性的 男性的
納品ファイル
• 高解像度JPG (.jpg)
• イラストレーター形式 (.ai)
補足説明
開催内容の資料を送ります。
また、講師のプロフィールを送ります。

クレジットは、写真提供:森川拓事務所もしくは(c)Taku Morikawa Office等とご表記ください。
皆様お世話になっております。

ポスターの写真は、スポンサーの関係で前回添付した画像以外は基本的には、使用ができませんのでご了承ください。
そのほかの写真を使いたい場合は、一度こちらに確認いただきます様よろしくお願いします。
皆様いつもお世話になっております。
画像が添付されておりませんでした。大変失礼しました。

ご対応どうぞよろしくお願いします。
左上にPRVマークをつけていただきます様よろしくお願いします。
なお、空白とマークの位置はデータのバランスを維持していただきます様お願いします。
■ 選んだ理由

全体の色合いも非常によかったです。ダイナミックな雰囲気と仲間の絆のイメージをうまく表現していただけたと思います。

■ 提案者全員のお礼・コメント

皆様、たくさんのご応募ありがとうございました。こちらのイメージをうまく呼んでいただいたかと思います。
次回もどうぞよろしくお願いします。

```html
<!DOCTYPE html>
<html lang="ja">
<head>
<meta charset="utf-8">
<title>森川拓 講演会 仲間の絆</title>
<link rel="stylesheet" href="https://fonts.googleapis.com/css2?family=Noto+Sans+JP:wght@400;700;900&family=Noto+Serif+JP:wght@500;900&family=Yuji+Syuku&display=swap">
<style>
:root{
  --navy-deep:#0a2350;
  --navy:#174583;
  --sky:#4d86c6;
  --ink:#1b1b1b;
  --red:#c8121b;
  --white:#ffffff;
  --paper:#f4f7fb;
  --mark:#1f5fb0;
}
*{margin:0;padding:0;box-sizing:border-box}
html,body{width:847px;height:1200px;overflow:hidden;background:var(--white)}
.poster{position:relative;width:847px;height:1200px;overflow:hidden;background:var(--white);font-family:"Noto Sans JP",sans-serif;color:var(--ink)}
.abs{position:absolute}

.org-mark{left:14px;top:12px;z-index:3;display:flex;align-items:center;gap:8px;color:var(--white);font-weight:900;font-size:30px;letter-spacing:1px}
.org-mark .dot{width:26px;height:26px;border-radius:50%;background:var(--white)}

.hero-photo{left:0;top:0;width:535px;height:560px;background:radial-gradient(ellipse at 45% 45%,#b48a6a 0%,#7a5b48 28%,#5e6f88 55%,#cfd9e6 100%)}
.photo-credit{left:8px;top:540px;font-size:9px;color:var(--white)}

.title-main{left:548px;top:22px;font-family:"Yuji Syuku",serif;font-size:92px;line-height:1;letter-spacing:2px}
.subtitle{left:548px;top:140px;writing-mode:vertical-rl;font-family:"Noto Serif JP",serif;font-weight:500;font-size:27px;letter-spacing:4px}
.title-bond{left:590px;top:140px;font-family:"Yuji Syuku",serif;font-size:255px;line-height:1;color:var(--red)}

.lower{left:0;top:560px;width:847px;height:640px;background:linear-gradient(180deg,var(--navy) 0%,var(--navy-deep) 55%,var(--navy) 100%)}
.photo-ice{left:0;top:560px;width:212px;height:130px;background:linear-gradient(160deg,#e9f1fa,#8fb5dc 60%,#3c6ea6)}
.photo-peak{left:216px;top:560px;width:216px;height:130px;background:linear-gradient(180deg,#2d5d9c,#9fbfe0 55%,#f2f5f9)}

.speaker-role{left:22px;top:702px;font-family:"Noto Serif JP",serif;font-size:22px;color:var(--white);letter-spacing:2px}
.speaker-name{left:16px;top:726px;font-family:"Noto Serif JP",serif;font-weight:900;font-size:108px;line-height:1;color:var(--white);letter-spacing:4px}
.talk-label{left:360px;top:700px;writing-mode:vertical-rl;font-family:"Noto Serif JP",serif;font-weight:900;font-size:38px;color:var(--white);letter-spacing:4px}

.event-info{left:22px;top:858px;width:420px;color:var(--white);font-size:16px;line-height:1.55}
.event-info b{font-weight:700}

.photo-team{left:0;top:950px;width:432px;height:200px;background:linear-gradient(170deg,#5f8ed0 0%,#b9cde6 45%,#e9eef5 70%,#b33a3a 100%)}

.portrait{left:568px;top:566px;width:156px;height:118px;background:linear-gradient(180deg,#6b8fbf,#2f4d7a)}
.profile{left:456px;top:694px;width:378px;color:var(--white)}
.profile h2{font-size:16px;font-weight:700;margin-bottom:4px}
.profile .lead{font-size:15px;font-weight:700;margin-bottom:6px}
.profile p{font-size:12.5px;line-height:1.6;text-align:justify}

.program{left:456px;top:1000px;width:380px;height:150px;background:var(--paper);border-radius:4px;padding:10px 14px;font-size:12.5px;line-height:1.6;color:var(--ink)}
.program h3{font-size:13px;font-weight:700;color:var(--navy)}

.site{left:0;top:1160px;width:847px;text-align:center;color:var(--white);font-size:14px;letter-spacing:1px}
</style>
</head>
<body>
<div class="poster">
  <div class="abs hero-photo" role="img" aria-label="雪山で帽子とゴーグルを身につけた登山家の写真"></div>
  <div class="abs org-mark"><span class="dot"></span>PRV</div>
  <div class="abs photo-credit">写真提供:森川拓事務所</div>

  <div class="abs title-main">仲間の</div>
  <div class="abs subtitle">〜夢と希望に向かって〜</div>
  <div class="abs title-bond">絆</div>

  <div class="abs lower"></div>
  <div class="abs photo-ice" role="img" aria-label="氷河とクレバスの写真"></div>
  <div class="abs photo-peak" role="img" aria-label="青空の下の雪山の写真"></div>

  <div class="abs speaker-role">アルピニスト</div>
  <div class="abs speaker-name">森川拓</div>
  <div class="abs talk-label">講演会</div>

  <div class="abs event-info">
    <b>日時:</b>平成25年7月14日(日) 14:00〜16:30(開場13:30)<br>
    <b>場所:</b>みなと市民会館 ホール<br>
    愛知県みなと市東町12-3 TEL:0586-00-1234
  </div>

  <div class="abs photo-team" role="img" aria-label="山頂で旗を掲げる登山隊の写真"></div>

  <div class="abs portrait" role="img" aria-label="講師の顔写真"></div>
  <section class="abs profile">
    <h2>【プロフィール】</h2>
    <div class="lead">森川 拓(もりかわ たく)アルピニスト</div>
    <p>若くして各大陸の最高峰を目指し、数々の山に挑み続けてきた登山家。世界の高峰での経験をもとに、山の清掃活動や環境を守る取り組みを続けている。近年は子どもたちに向けた学びの場づくりや、被災地を支える活動にも力を注ぎ、仲間と共に夢を追う大切さを各地の講演で伝えている。</p>
  </section>

  <div class="abs program">
    <h3>◆講演内容</h3>
    ・山で学んだ「仲間の絆」と挑戦の心<br>
    ・世界の高峰で見た自然と環境の今<br>
    ・清掃登山から始まった地域との歩み<br>
    ・夢と希望に向かう次の世代へのメッセージ
  </div>

  <div class="abs site">公式ウェブサイト:www.morikawa-taku.example</div>
</div>
</body>
</html>
```